I would like a stylish low key card that represents my Cedar Lodge. A boutique rental property . This property is of the highest standard and I wish the card to covey this without being old fashion

Industry/Entity Type

Boutique

Contact Information for Business Card

Tess Varlowe
0438207519
tess.varlowe@varlowe.com.au Cedar Lodge

```html
<!DOCTYPE html>
<html lang="en">
<head>
<meta charset="utf-8">
<title>The Cedar Lodge – Business Card</title>
<link rel="stylesheet" href="https://fonts.googleapis.com/css2?family=Lato:wght@400;700&family=Barlow+Condensed:wght@400;600&display=swap">
<style>
  :root {
    --ink: #020405;
    --ink-soft: #0b0d0e;
    --glow: #2a2c2d;
    --mist: #8a8c8d;
    --paper: #ffffff;
    --accent: #1aa6dc;
  }
  * { margin: 0; padding: 0; box-sizing: border-box; }
  html, body {
    width: 1200px;
    height: 693px;
    overflow: hidden;
    background: var(--ink);
  }
  .card {
    position: relative;
    width: 1200px;
    height: 693px;
    overflow: hidden;
    background:
      radial-gradient(ellipse 520px 360px at 600px -40px, var(--glow) 0%, var(--ink-soft) 55%, var(--ink) 100%);
  }
  .water-surface {
    position: absolute;
    left: 140px;
    top: 440px;
    width: 920px;
    height: 253px;
    background:
      radial-gradient(ellipse 390px 70px at 460px 110px, #a8aaab 0%, #6a6c6d 28%, #2b2d2e 62%, transparent 100%),
      radial-gradient(ellipse 460px 140px at 460px 60px, rgba(120,122,123,0.55) 0%, rgba(40,42,43,0.3) 55%, transparent 100%);
  }
  .title {
    position: absolute;
    left: 0;
    right: 0;
    top: 402px;
    text-align: center;
    font-family: "Lato", sans-serif;
    font-weight: 400;
    font-size: 31px;
    letter-spacing: 30px;
    padding-left: 30px;
    color: var(--paper);
    line-height: 1;
  }
  .tagline {
    position: absolute;
    left: 0;
    right: 0;
    top: 457px;
    text-align: center;
    font-family: "Lato", sans-serif;
    font-weight: 700;
    font-size: 13px;
    letter-spacing: 15px;
    padding-left: 15px;
    color: var(--paper);
    line-height: 1;
  }
  .contact {
    position: absolute;
    left: 0;
    right: 0;
    top: 627px;
    text-align: center;
    font-family: "Barlow Condensed", sans-serif;
    font-weight: 400;
    font-size: 20px;
    color: var(--paper);
    line-height: 1;
  }
  .contact .name {
    color: var(--accent);
    font-weight: 600;
    margin: 0 2px;
  }
</style>
</head>
<body>
  <div class="card">
    <div class="water-surface" role="img" aria-label="Dark water surface with concentric ripples spreading under a soft spotlight"></div>
    <h1 class="title">THE CEDAR LODGE</h1>
    <p class="tagline">A BOUTIQUE RENTAL PROPERTY</p>
    <p class="contact"><span class="phone">0438207519</span> <span class="name">Tess Varlowe</span> <span class="email">tess.varlowe@varlowe.com.au</span></p>
  </div>
</body>
</html>
```